Nonprofit K-8 Tillerby School. Elementary education ( please google Tillerby Schools)

We are a nonprofit Tillerby School in the U.S.
We need to advertise our school using yard signs. The information should be easy to see from a distance. Clear and concise, using large print without additional design outside of the logo itself. It should have our logo as the header, with the following text centered below the logo:
Open House!
Feb 10th, March 10th and April 21st.
Call 555 417-9086 for more information

Target Market(s)

Parents of children between ages of 5 yrs to 13yrs old

Industry/Entity Type

School

Font styles to use
Other font styles liked:
• Formal436bt

Colors
ec1f27
ffffff

Requirements
Must have
• It must have our uploaded logo as the header, and the following information below using the font Formal436bt:
• Open House!
• Feb 10th, March 10th and April 21st.
• Call 555 417-9086 for more information
Should not have
• Any other color but the red and white indicated on our logo

```html
<!DOCTYPE html>
<html lang="en">
<head>
<meta charset="utf-8">
<title>Tillerby School — Open House Yard Sign</title>
<link rel="stylesheet" href="https://fonts.googleapis.com/css2?family=Marcellus&display=swap">
<style>
  :root {
    --brand-red: #ec1f27;
    --sign-white: #ffffff;
    --sign-paper: #f1f1f1;
    --ink: #111111;
    --backdrop: #e4e4e4;
  }
  * { margin: 0; padding: 0; box-sizing: border-box; }
  html, body {
    width: 1200px;
    height: 1000px;
    overflow: hidden;
    background: var(--backdrop);
  }
  .yard-sign {
    position: absolute;
    left: 268px;
    top: 58px;
    width: 664px;
    height: 884px;
    background: linear-gradient(180deg, var(--sign-white) 0%, var(--sign-paper) 100%);
    font-family: "Marcellus", serif;
    text-align: center;
  }
  .sign-header {
    position: absolute;
    left: 0;
    right: 0;
    top: 78px;
    display: flex;
    justify-content: center;
    align-items: center;
    gap: 16px;
  }
  .header-mark {
    width: 30px;
    height: 30px;
    background: var(--brand-red);
  }
  .school-name {
    font-size: 36px;
    line-height: 1;
    color: var(--ink);
    letter-spacing: 0.5px;
    text-transform: uppercase;
  }
  .headline {
    position: absolute;
    left: 0;
    right: 0;
    top: 232px;
    color: var(--brand-red);
    font-size: 150px;
    line-height: 128px;
    font-weight: 400;
    text-transform: uppercase;
    letter-spacing: 1px;
  }
  .headline span { display: block; }
  .event-dates {
    position: absolute;
    left: 0;
    right: 0;
    top: 528px;
    color: var(--brand-red);
    font-size: 44px;
    line-height: 56px;
  }
  .contact-band {
    position: absolute;
    left: 0;
    right: 0;
    top: 699px;
    height: 125px;
    background: var(--brand-red);
    color: var(--sign-white);
    padding-top: 12px;
  }
  .contact-call {
    font-size: 50px;
    line-height: 60px;
  }
  .contact-note {
    font-size: 31px;
    line-height: 36px;
  }
</style>
</head>
<body>
  <main class="yard-sign">
    <header class="sign-header">
      <span class="header-mark" aria-hidden="true"></span>
      <span class="school-name">Tillerby School</span>
    </header>
    <h1 class="headline"><span>Open</span><span>House!</span></h1>
    <p class="event-dates">Feb 10th, March 10th<br>and April 21st.</p>
    <section class="contact-band">
      <p class="contact-call">Call 555 417-9086</p>
      <p class="contact-note">for more information</p>
    </section>
  </main>
</body>
</html>
```